New Law Firm Corporate Identity Project

Newly started law firm needs a corporate identity. The theme behind the corporate identity should be simple and elegant, yet professional.
What I need as part of this corporate identity kit (CIK) is a designed logo, letterhead, and business card.
Also, I would like to have an easily transferable electronic version of whatever you design, so that I can copy and paste this logo, etc. on Microsoft Word, for example. I would like the delivery of the logo, business card, and letterhead in high-res PSD and AI formats in CS1 and CS3, which can be resized later to any resolution possible (print ready included). I will then own the rights to the content once the work has been paid for. Since I will need multiple formats - .psd (CS1 and CS3), .ai (CS1 and CS3), .jpg, and .gif.
The name of the law firm is "Law Offices of Marcus Pell, APC". I would like my initials, "M" and "P" incorporated into the logo
The logo and CIK that I prefer would not look like the traditional law firm logo, with a guy being arrested, or of a building, or of the blindfolded lady balancing a scale. I prefer something modern and trendy, yet without the logo or CIK being too bland, too much, or looking “overcrowded”.
I'm not too particular on the color combinations, but I would like my logo and letterhead to stand out and look smart in terms of color combinations and design. Furthermore, I would like my logo to still be clearly seen after it has been photocopied.
Please use your creativity and create something original, such as hand-drawn art, as opposed to using clip-art.
Thanks in advance!
Updates
Project Deadline Extended
Reason: I changed the status of the project to guaranteed payment, and therefore, would like to see more logo options before deciding on which one to select. Thanks, and please keep submitting your proposals.
Industry/Entity Type
Electronic
Logo Text
Law Offices of Marcus Pell, APC. Incorporated into the actual logo are the letters "M" and "P".
Look and feel
Each slider illustrates characteristics of the customer's brand and the style your logo design should communicate.

```html
<!DOCTYPE html>
<html lang="en">
<head>
<meta charset="utf-8">
<title>Marcus Pell, APC — Stationery</title>
<link rel="stylesheet" href="https://fonts.googleapis.com/css2?family=Cinzel:wght@400&family=EB+Garamond:wght@400&display=swap">
<style>
  :root{
    --paper:#ffffff;
    --stage:#ffffff;
    --edge:#2b2b2b;
    --navy:#1c1f4a;
    --ink:#333844;
    --accent:#2f5fd0;
    --band-deep:#1a1a8c;
    --band-mid:#2f3fd8;
    --band-light:#8fb4ee;
  }
  *{box-sizing:border-box;margin:0;padding:0}
  html,body{width:1200px;height:900px;overflow:hidden;background:var(--stage)}
  .canvas{position:relative;width:1200px;height:900px}

  .sheet{position:absolute;background:var(--paper);border:1.5px solid var(--edge)}
  .letterhead{left:166px;top:60px;width:548px;height:780px}
  .card{width:234px;height:148px}
  .card--front{left:792px;top:260px}
  .card--back{left:792px;top:430px}

  .brand{position:absolute;display:flex;align-items:center;gap:7px;color:var(--navy);
    font-family:"Cinzel",serif;font-weight:400;line-height:1}
  .brand__square{display:block;background:var(--navy)}
  .brand__name{display:flex;flex-direction:column;gap:3px}
  .brand__line-small{font-size:11px}
  .brand__line-large{font-size:14px;letter-spacing:.2px}

  .letterhead .brand{left:14px;top:24px}
  .letterhead .brand__square{width:36px;height:36px}
  .card--front .brand{left:28px;top:52px}
  .card--front .brand__square{width:32px;height:32px}
  .card--front .brand__line-small{font-size:10px}
  .card--front .brand__line-large{font-size:12.5px}

  .contact{position:absolute;font-family:"EB Garamond",serif;font-size:8px;line-height:10px;color:var(--ink)}
  .contact .label{color:var(--accent)}
  .contact .web{color:var(--accent)}
  .letterhead .contact{left:330px;top:26px}

  .holder{position:absolute;left:16px;top:34px;font-family:"Cinzel",serif;font-size:10px;color:var(--navy)}
  .holder .label{color:var(--accent);font-size:10px}
  .card--back .contact--left{left:16px;top:56px;font-size:6.5px;line-height:9px}
  .card--back .contact--right{left:132px;top:56px;font-size:6.5px;line-height:9px}

  .band{position:absolute;left:0;right:0;
    background:linear-gradient(90deg,var(--band-deep) 0%,var(--band-mid) 35%,var(--band-light) 55%,var(--band-mid) 75%,var(--band-deep) 100%)}
  .letterhead .band{bottom:3px;height:30px}
  .card--back .band{bottom:4px;height:18px}
</style>
</head>
<body>
<main class="canvas">

  <section class="sheet letterhead" aria-label="Letterhead">
    <div class="brand">
      <span class="brand__square"></span>
      <span class="brand__name">
        <span class="brand__line-small">Law Offices of</span>
        <span class="brand__line-large">Marcus Pell, APC.</span>
      </span>
    </div>
    <address class="contact">
      <span class="label">office</span> 1420 Alder Street no. 12, Fairview CA 20145<br>
      p. 555 010 2244 | e. marcus-pell@mailbox.com<br>
      <span class="web">www.marcus-pell.com</span>
    </address>
    <div class="band" role="img" aria-label="Footer band of blue squares shading from deep to light blue"></div>
  </section>

  <section class="sheet card card--front" aria-label="Business card front">
    <div class="brand">
      <span class="brand__square"></span>
      <span class="brand__name">
        <span class="brand__line-small">Law Offices of</span>
        <span class="brand__line-large">Marcus Pell, APC.</span>
      </span>
    </div>
  </section>

  <section class="sheet card card--back" aria-label="Business card back">
    <p class="holder"><span class="label">OWNER</span> Marcus Pell, APC.</p>
    <address class="contact contact--left">
      <span class="label">office</span> 1420 Alder Street no. 12,<br>
      Fairview CA 20145<br>
      p. 555 010 2244
    </address>
    <address class="contact contact--right">
      e. marcus-pell@mailbox.com<br>
      <span class="web">www.marcus-pell.com</span>
    </address>
    <div class="band" role="img" aria-label="Footer band of blue squares shading from deep to light blue"></div>
  </section>

</main>
</body>
</html>
```